Eycatcher Flyer
Zielgruppe
Infos auf www.lumawerk-beratung.ch
Lebensberatung, Seminare, persönliche Weiterbildung,Medium
Aufgabenstellung
Suche ein Design für einen coolen, modernen, mystischen exklusiven(Image) Flyer. Format A4 Längs gefaltet (Endformat A5).
Flyer Titel Liebe dein Leben - Liebe dich selbst eventuell auch auf englisch love yourself and celebrates your life
oder vielleicht hat jemand noch einen besseren Slogan Vorschlag
Habe im Anhang ein Dokument mit Text kann ganz oder auszugweise verwendet werden. (Handelt sich um einen ersten Entwurf mögliche Rechtschreibfehler enthalten)
Ansonsten Inputs aus der Hp holen.
Lieblingsfarben Rot,Pink,Giftgrün,Gold,Schwarz, Gelb,

```html
<!DOCTYPE html>
<html lang="de">
<head>
<meta charset="utf-8">
<title>Lumawerk – Flyer Liebe dein Leben</title>
<link rel="stylesheet" href="https://fonts.googleapis.com/css2?family=Fira+Sans+Condensed:ital,wght@0,300;0,400;0,600;1,300;1,400&family=Open+Sans:wght@400;600&display=swap">
<style>
:root{
  --stage:#cfcfcf;
  --ink:#0b0b0b;
  --pink:#c8175d;
  --pink-soft:#e0407e;
  --white:#f4f4f4;
  --grey:#bdbdbd;
  --gold:#b8872c;
}
*{box-sizing:border-box;margin:0;padding:0}
html,body{width:1200px;height:900px;overflow:hidden}
body{background:var(--stage);font-family:"Open Sans",sans-serif;position:relative}
.spread{position:absolute;left:60px;width:1080px;display:flex;box-shadow:0 6px 18px rgba(0,0,0,.25)}
.spread--outer{top:40px;height:250px}
.spread--inner{top:330px;height:530px}
.panel{position:relative;width:540px;height:100%;background:var(--ink);overflow:hidden;color:var(--white)}
.panel + .panel{border-left:1px solid #1c1c1c}
.ornament{position:absolute;background:
  radial-gradient(ellipse at 30% 40%,rgba(200,23,93,.75),rgba(200,23,93,0) 60%),
  radial-gradient(ellipse at 75% 70%,rgba(200,23,93,.55),rgba(200,23,93,0) 55%)}
.photo{position:absolute}
.photo--compass{left:0;top:105px;width:120px;height:145px;background:radial-gradient(circle at 60% 45%,#e9c05a,var(--gold) 40%,#3a2608 80%,var(--ink))}
.photo--stones{left:0;top:215px;width:190px;height:250px;background:radial-gradient(ellipse at 50% 60%,#a8a48c,#6b6856 45%,#1a1a16 85%)}
.photo--circle{right:0;top:120px;width:185px;height:410px;background:linear-gradient(180deg,#2a2a2a,#8c8a86 40%,#c9c3bc 70%,#5a5550)}
.brand{position:absolute;display:flex;align-items:center;gap:10px}
.brand__dot{width:22px;height:22px;border-radius:50%;background:var(--pink)}
.brand__name{font-family:"Fira Sans Condensed",sans-serif;font-weight:300;font-size:34px;letter-spacing:2px;color:var(--white)}
.brand__tag{position:absolute;font-family:"Fira Sans Condensed",sans-serif;font-weight:300;font-size:12px;color:var(--white)}
.url{font-family:"Fira Sans Condensed",sans-serif;font-weight:300;color:var(--pink-soft)}
.headline{position:absolute;left:30px;top:28px;font-family:"Fira Sans Condensed",sans-serif;font-weight:300;font-size:29px;letter-spacing:.5px;color:var(--white);white-space:nowrap}
.subline{position:absolute;left:32px;top:68px;font-family:"Fira Sans Condensed",sans-serif;font-style:italic;font-weight:300;font-size:17px;color:var(--pink)}
.script{font-family:"Fira Sans Condensed",sans-serif;font-style:italic;font-weight:300;color:var(--pink);line-height:1.05}
.title-vertical{position:absolute;left:96px;top:175px;font-size:26px;transform:rotate(-90deg);transform-origin:left top;white-space:nowrap;top:190px}
.title-soul{position:absolute;left:20px;top:22px;font-size:30px}
.col{position:absolute;font-size:9.6px;line-height:1.48;color:var(--white)}
.col p{margin-bottom:8px}
.col h3{font-family:"Open Sans",sans-serif;font-size:9.6px;font-weight:600;color:var(--pink-soft);margin-bottom:2px}
.col ul{list-style:none;margin:0 0 8px}
.col li::before{content:"› ";color:var(--pink-soft);font-weight:600}
.box{position:absolute;background:var(--pink);color:var(--white);font-size:9.6px;line-height:1.45;padding:10px 12px}
.box--url{font-family:"Fira Sans Condensed",sans-serif;font-weight:300;font-size:18px;padding:8px 12px}
</style>
</head>
<body>

<section class="spread spread--outer">
  <article class="panel panel--back">
    <div class="ornament" style="left:150px;top:0;width:390px;height:55px" role="img" aria-label="Pinke florale Rankenornamente am oberen Rand"></div>
    <div class="ornament" style="left:0;top:40px;width:120px;height:210px" role="img" aria-label="Pinke florale Rankenornamente am linken Rand"></div>
    <div class="brand" style="left:170px;top:95px"><span class="brand__dot"></span><span class="brand__name">LUMAWERK</span></div>
    <span class="brand__tag" style="left:250px;top:140px">Die Sprache des Herzens</span>
    <span class="url" style="position:absolute;left:170px;top:158px;font-size:21px">www.lumawerk-beratung.ch</span>
  </article>
  <article class="panel panel--front">
    <h1 class="headline">LIEBE DEIN LEBEN – LIEBE DICH SELBST</h1>
    <p class="subline">love yourself and celebrates your life</p>
    <div class="photo photo--compass" role="img" aria-label="Foto eines goldenen Kompasses"></div>
    <div class="brand" style="left:300px;top:150px"><span class="brand__dot"></span><span class="brand__name">LUMAWERK</span></div>
    <span class="brand__tag" style="left:385px;top:196px">Die Sprache des Herzens</span>
  </article>
</section>

<section class="spread spread--inner">
  <article class="panel panel--inner-left">
    <div class="ornament" style="left:0;top:0;width:90px;height:530px" role="img" aria-label="Pinke florale Rankenornamente am linken Rand"></div>
    <h2 class="script title-vertical">Love your life</h2>
    <div class="col" style="left:150px;top:26px;width:185px">
      <p>Wir rennen und tun, wir sind oft so gefangen im Rad des Aktivismus, dass wir ganz vergessen zu sein. Wir sind so beschäftigt damit etwas zu verändern, dass wir dabei vollkommen vergessen unser Leben zu geniessen und mit Liebe zu erfüllen.</p>
      <h3>Annahme – Wertschätzung –<br>Achtung atmosphäre fast vergessene Worte.</h3>
      <p>Doch diese Worte haben eine power. Es sind Worte mit Wurzeln. Worte die einem eine Heimat geben. Eine Heimat in sich selber und eine Heimat im Leben. Eine Heimat die unabhängig von geografischen Orten und äusseren Umständen ist.</p>
      <p>Gegebenheiten akzeptieren. Körperliche ebenso wie psychische. Wir sind was wir sind – Menschen mit Stärken und Schwächen.</p>
      <p>Wertschätzen was ist und mit Achtung verändern was möglich und sinnvoll ist. Annehmen und akzeptieren was ist, so bleiben will wie es ist.</p>
    </div>
    <div class="col" style="left:350px;top:26px;width:178px">
      <p>Wenn du nicht weißt wo du bist, kannst du auch nicht wissen wo du landest wenn du dich auf den Weg machst. Selbst dann wenn du die Himmelsrichtungen erkennst oder eine Karte besitzt. Erst musst du deinen Ausgangsort kennen.</p>
      <p>Wenn du dein Ziel kennst musst du auch wissen wo du jetzt stehst. So kannst du den besten Weg zur Erreichung deines Zieles finden, und die für dich optimale Reiseroute planen.</p>
      <ul>
        <li>Was habe ich</li>
        <li>Wo will ich hin</li>
        <li>Warum</li>
        <li>Was trägt es zu meinem Leben bei, wenn ich dieses Ziel erreiche</li>
        <li>Worauf verzichte ich wenn ich dieses Ziel erreiche</li>
      </ul>
    </div>
    <p class="box" style="left:345px;top:440px;width:195px">Oft sind wir so damit beschäftigt jemand (etwas) zu werden, dass wir ganz vergessen jemand zu sein.</p>
  </article>

  <article class="panel panel--inner-right">
    <div class="ornament" style="left:200px;top:0;width:340px;height:60px" role="img" aria-label="Pinke florale Rankenornamente am oberen Rand"></div>
    <h2 class="script title-soul">Der Seele<br>Sorge tragen</h2>
    <div class="photo photo--stones" role="img" aria-label="Foto gestapelter Steine mit brennendem Teelicht"></div>
    <div class="col" style="left:200px;top:40px;width:150px">
      <h3>Meditation</h3>
      <p>Die Vorteile der Meditation sind vielfältig. Meditieren hat gesundheitliche Vorteile und bietet die Möglichkeit, mehr Ausgeglichenheit, Erfüllung und Freude zu erfahren. Herausforderungen im Beruf und Privatleben sind leichter zu meistern. Sie entspannt Körper und Geist. Damit verringert sich das Risiko von stressbedingten Krankheiten. Außerdem steigert sich die Konzentrationsfähigkeit.</p>
      <h3>Heilende Gespräche</h3>
      <p>Heilende Gespräche gehen weit über das hinaus, was man sich landläufig unter dem Begriff „Gespräch" vorstellt. Diese Gespräche finden auf einer anderen Ebene statt. Gemeinsam betreten wir ein Feld, in dem eine Kommunikation von Herz zu Herz und von Seele zu Seele stattfinden kann.</p>
    </div>
    <div class="col" style="left:362px;top:48px;width:170px">
      <h3>Frauen-Heilkreis</h3>
      <p>Die weibliche Weisheit und Kraft wurde seit zu langer Zeit ignoriert, unterdrückt und geschwächt. Deshalb ist es jetzt wichtig die weibliche Kraft wieder zu entdecken und zu fördern. Frauen tragen das alte Wissen der weiblichen Weiblichkeit tief in ihrem Inneren. Die Körper von uns Frauen den Zyklen des Mondes unterliegen, ist unsere Weisheit direkt mit dem Himmel verbunden. Das nährende und sinnlich weibliche des die Gabe hat durch bedingungslose Liebe zu handeln, kann wieder mehr Frieden und Harmonie in unser persönliches Umfeld und auch in die Welt bringen.</p>
    </div>
    <div class="photo photo--circle" style="top:300px;height:230px" role="img" aria-label="Foto einer Gruppe von Frauen im Kreis liegend"></div>
    <p class="box box--url" style="left:355px;top:465px;width:170px">www.lumawerk-beratung.ch</p>
  </article>
</section>

</body>
</html>
```